Native Bush Healing Balms/Oils needs label/logo

Kiwaru Stillness is our name, we are a new startup business in New Zealand. Kiwaru means love in Maori. We make native bush balms, oils, tinctures, teas and do mirimiri which is a form of Maori healing. We are wanting a design for a balm label first off, however keep in mind that we will be wanting to transfer the logo across to other products, like the teas, t-shirts and even a calico tote bag! We would like it so we can edit the ingredients if possible.

We have had the 'flower/heart logo' made up to replace the 'o' in kiwaru. This we would like in a metallic electric purple/violet colour. We would like the 'kiwaru stillness' in silver. Please make sure the macron is above the last ā in kiwaru. We are open to other colour options and other styles of the flower/heart logo.

We would like the overall effect to be simple, clean, minimalist, bright. Colours we like are electric purple/violet, silver, then thinking of different colours for the different types/flavours, probably on a matte sticker. Fonts we think will suit are an italic curved/rounded font for the kiwaru and a capital font for the vibrations.

We have had a quick mock up of the labels which is attached. Also attached is a photo of my current balm and teas, and label ideas that I like. The drawings show a sticker for the lid with a safety tab.

Looking forward to seeing your wonderful designs! :)

Target Market(s)

People into natural self healing, who want traditionally made high vibrational, top end products

Industry/Entity Type

Health And Wellness

Requirements
Must have
• Silver writing on logo, or front of jar or lid.
• 'Made in Aotearoa' on jar
Nice to have
• Colours I like are hot pink, yellow, bright teal green, royal purple
Should not have
• Should not be cluttered

```html
<!DOCTYPE html>
<html lang="en">
<head>
<meta charset="utf-8">
<title>Kiwaru Stillness — Label Set</title>
<link rel="stylesheet" href="https://fonts.googleapis.com/css2?family=Jost:wght@300;400&family=Source+Sans+3:wght@400&display=swap">
<style>
  :root {
    --paper: #ffffff;
    --ink: #000000;
    --violet: #7a3f9c;
    --silver: #e6e6e6;
    --muted: #8a8a8a;
    --teal: #0088a8;
    --royal: #76479b;
    --pink: #ae2190;
    --gold: #fcbe15;
  }
  * { box-sizing: border-box; margin: 0; padding: 0; }
  html, body { width: 1200px; height: 735px; overflow: hidden; background: var(--paper); }
  body { position: relative; font-family: "Jost", sans-serif; }

  .wordmark {
    position: absolute; text-align: center;
    font-family: "Jost", sans-serif; font-weight: 400;
    color: var(--violet); line-height: 1;
  }
  .wordmark__name, .wordmark__tag { display: block; }
  .wordmark__tag { text-transform: uppercase; }

  .balm-label {
    position: absolute; left: 57px; width: 815px; height: 184px;
    background: var(--ink); color: var(--silver);
  }
  .balm-label--spiral { top: 61px; }
  .balm-label--ruled { top: 278px; }
  .balm-label .wordmark { left: 149px; width: 200px; top: 14px; }
  .balm-label .wordmark__name { font-size: 38px; }
  .balm-label .wordmark__tag { font-size: 15px; letter-spacing: 3px; margin-top: 1px; }

  .product-name {
    position: absolute; left: 79px; width: 340px; top: 88px;
    text-align: center; font-weight: 300; font-size: 38px; letter-spacing: 0.5px; line-height: 1.2;
  }
  .net-size {
    position: absolute; left: 149px; width: 200px; text-align: center;
    font-family: "Source Sans 3", sans-serif;
  }
  .balm-label--spiral .net-size { top: 152px; color: var(--violet); font-size: 9.5px; }
  .balm-label--ruled .net-size { top: 157px; color: var(--silver); font-size: 7px; }

  .pattern-strip { position: absolute; background: var(--violet); opacity: 0.85; border-radius: 3px; }
  .pattern-strip--vertical { width: 6px; height: 98px; top: 52px; }
  .pattern-strip--left { left: 525px; }
  .pattern-strip--right { left: 762px; }
  .pattern-strip--band { left: 189px; width: 121px; height: 5px; top: 143px; }

  .rule { position: absolute; width: 1px; height: 71px; top: 63px; background: var(--silver); }
  .rule--left { left: 536px; }
  .rule--right { left: 753px; }

  .balm-copy {
    position: absolute; left: 555px; width: 190px; top: 65px;
    font-family: "Source Sans 3", sans-serif; font-size: 7.5px; line-height: 1.45; color: var(--silver);
  }
  .balm-copy p + p { margin-top: 5px; }

  .lid-sticker { position: absolute; left: 901px; top: 59px; width: 270px; height: 186px; }
  .lid-tab {
    position: absolute; left: 177px; top: 78px; width: 89px; height: 31px;
    border: 1px solid var(--ink); border-radius: 4px; background: var(--paper);
  }
  .lid-tab__inner {
    position: absolute; left: 3px; top: 3px; right: 3px; bottom: 3px;
    background: var(--ink); color: var(--muted);
    font-size: 7px; letter-spacing: 0.4px; display: flex; align-items: center; justify-content: flex-end; padding-right: 5px;
  }
  .lid-ring {
    position: absolute; left: 2px; top: 2px; width: 182px; height: 182px;
    border-radius: 50%; border: 1px solid var(--ink); background: var(--paper);
  }
  .lid-face {
    position: absolute; left: 4px; top: 4px; width: 172px; height: 172px;
    border-radius: 50%; background: var(--ink);
  }
  .lid-face .wordmark { left: 0; width: 172px; top: 54px; }
  .lid-face .wordmark__name { font-size: 44px; }
  .lid-face .wordmark__tag { font-size: 17px; letter-spacing: 3px; }

  .tea-card { position: absolute; top: 522px; width: 238px; height: 158px; color: var(--paper); }
  .tea-card--manuka { left: 60px; background: var(--teal); }
  .tea-card--kumarahou { left: 321px; background: var(--royal); }
  .tea-card--tataramoa { left: 582px; background: var(--pink); }
  .tea-card--kawakawa { left: 842px; background: var(--gold); }
  .tea-card .wordmark { left: 19px; width: 200px; top: 18px; color: var(--ink); }
  .tea-card--manuka .wordmark { top: 10px; }
  .tea-card .wordmark__name { font-size: 30px; }
  .tea-card .wordmark__tag { font-size: 11.5px; letter-spacing: 2.5px; }
  .tea-card__name {
    position: absolute; left: 0; width: 238px; top: 77px; text-align: center;
    font-weight: 300; font-size: 25px; white-space: nowrap; line-height: 1.2;
  }
  .tea-card__band {
    position: absolute; left: 70px; width: 98px; height: 5px; top: 111px;
    background: var(--paper); opacity: 0.8; border-radius: 3px;
  }
  .tea-card__benefits {
    position: absolute; left: 24px; width: 190px; top: 124px; text-align: center;
    font-family: "Source Sans 3", sans-serif; font-size: 5px; line-height: 1.3; color: var(--ink);
  }
</style>
</head>
<body>

  <section class="balm-label balm-label--spiral">
    <div class="wordmark"><span class="wordmark__name">kiwaru</span><span class="wordmark__tag">stillness</span></div>
    <h1 class="product-name">KAWAKAWA</h1>
    <p class="net-size">HANDMADE BALM - 15 ML</p>
    <div class="pattern-strip pattern-strip--vertical pattern-strip--left" role="img" aria-label="Vertical koru spiral pattern in violet"></div>
    <div class="balm-copy">
      <p>I'm great on minor skin irritations, cuts, bites, rashes and more. Rub me lovingly, little and often.</p>
      <p>Made with Tanewai, sacred sounds and traditional knowledge from kawakawa oil, beeswax and kiwaru.</p>
      <p>friendbook:kiwaru/</p>
    </div>
    <div class="pattern-strip pattern-strip--vertical pattern-strip--right" role="img" aria-label="Vertical koru spiral pattern in violet"></div>
  </section>

  <section class="balm-label balm-label--ruled">
    <div class="wordmark"><span class="wordmark__name">kiwaru</span><span class="wordmark__tag">stillness</span></div>
    <h1 class="product-name">KAWAKAWA</h1>
    <div class="pattern-strip pattern-strip--band" role="img" aria-label="Horizontal wave pattern in violet"></div>
    <p class="net-size">HANDMADE BALM - 15 ML</p>
    <span class="rule rule--left"></span>
    <div class="balm-copy">
      <p>I'm great on minor skin irritations, cuts, bites, rashes and more. Rub me lovingly, little and often.</p>
      <p>Made with Tanewai, sacred sounds and traditional knowledge from kawakawa oil, beeswax and kiwaru.</p>
      <p>friendbook:kiwaru/</p>
    </div>
    <span class="rule rule--right"></span>
  </section>

  <section class="lid-sticker">
    <div class="lid-tab"><div class="lid-tab__inner">MEND THE SPIRIT</div></div>
    <div class="lid-ring">
      <div class="lid-face">
        <div class="wordmark"><span class="wordmark__name">kiwaru</span><span class="wordmark__tag">stillness</span></div>
      </div>
    </div>
  </section>

  <section class="tea-card tea-card--manuka">
    <div class="wordmark"><span class="wordmark__name">kiwaru</span><span class="wordmark__tag">stillness</span></div>
    <h2 class="tea-card__name">MANUKA TEA</h2>
    <div class="tea-card__band" role="img" aria-label="Wave pattern"></div>
    <p class="tea-card__benefits">ASTRINGENT, COUGHS, COLDS, KIDNEYS, BLADDER</p>
  </section>

  <section class="tea-card tea-card--kumarahou">
    <div class="wordmark"><span class="wordmark__name">kiwaru</span><span class="wordmark__tag">stillness</span></div>
    <h2 class="tea-card__name">KUMARAHOU TEA</h2>
    <div class="tea-card__band" role="img" aria-label="Wave pattern"></div>
    <p class="tea-card__benefits">EXPECTORANT, COUGHS, LUNGS, ASTHMA,<br>BRONCHITIS, BLOOD PURIFIER, KIDNEYS</p>
  </section>

  <section class="tea-card tea-card--tataramoa">
    <div class="wordmark"><span class="wordmark__name">kiwaru</span><span class="wordmark__tag">stillness</span></div>
    <h2 class="tea-card__name">TATARAMOA TEA</h2>
    <div class="tea-card__band" role="img" aria-label="Wave pattern"></div>
    <p class="tea-card__benefits">RELAXANT, GREAT FOR DEPRESSION, DIURETIC</p>
  </section>

  <section class="tea-card tea-card--kawakawa">
    <div class="wordmark"><span class="wordmark__name">kiwaru</span><span class="wordmark__tag">stillness</span></div>
    <h2 class="tea-card__name">KAWAKAWA TEA</h2>
    <div class="tea-card__band" role="img" aria-label="Wave pattern"></div>
    <p class="tea-card__benefits">HEALTH TONIC, GREAT FOR HEART, LUNGS, DIGESTION,<br>REDUCES INFLAMMATION</p>
  </section>

</body>
</html>
```